Stationary and Business Card
Medical Practice
I need single sided standard sized Business Card [3.5" x 2"]
Letter type / font / color is up to the designer.
Professional
Benedict Harwell, MD
Torrance Ridge-Velmont Building
Suite 460
4127 Almaden Avenue
La Jolla, CA 92037
contact@brinmoor-example.com
www.drharwell-example.com
Please use provided logo.
Please visit drharwell-example.com for any additional creative direction.
Do not include email address.
Please provide a version with www.drharwell-example.com on the back of the card and a version with the web address on the front.

```html
<!DOCTYPE html>
<html lang="en">
<head>
<meta charset="utf-8">
<title>Harwell Stationery Set</title>
<link href="https://fonts.googleapis.com/css2?family=Cinzel:wght@600&family=Open+Sans:wght@400;600&display=swap" rel="stylesheet">
<style>
  :root {
    --backdrop-light: #8a8a8a;
    --backdrop-dark: #5c5c5c;
    --paper: #ffffff;
    --brand-blue: #1f5fa8;
    --ink: #4a4a4a;
    --rule: #9a9a9a;
    --fold: #d4d4d4;
  }
  * { margin: 0; padding: 0; box-sizing: border-box; }
  html, body { width: 1200px; height: 626px; overflow: hidden; }
  body {
    position: relative;
    background: radial-gradient(ellipse at 50% 45%, var(--backdrop-light), var(--backdrop-dark));
    font-family: "Open Sans", sans-serif;
    color: var(--ink);
  }
  .sheet {
    position: absolute;
    background: var(--paper);
    box-shadow: 0 2px 6px rgba(0,0,0,.35);
  }
  .brand {
    display: flex;
    align-items: center;
    gap: 5px;
    font-family: "Cinzel", serif;
    font-weight: 600;
    color: var(--brand-blue);
    letter-spacing: .06em;
    line-height: 1;
  }
  .brand-square { background: var(--brand-blue); flex: none; }
  .contact {
    font-size: 5px;
    line-height: 1.55;
    color: var(--ink);
    border-left: 1px solid var(--rule);
    padding-left: 6px;
  }
  .contact .name { font-weight: 600; }

  /* Business card, front */
  .card-front { left: 34px; top: 199px; width: 187px; height: 99px;
    display: flex; flex-direction: column; align-items: center; justify-content: center; gap: 6px; }
  .card-front .brand { font-size: 15px; }
  .card-front .brand-square { width: 9px; height: 9px; }
  .card-front .web { font-size: 5px; letter-spacing: .08em; color: var(--ink); }

  /* Business card, back */
  .card-back { left: 34px; top: 312px; width: 187px; height: 101px;
    display: flex; align-items: center; padding-left: 10px; gap: 8px; }
  .card-back .brand { font-size: 11px; }
  .card-back .brand-square { width: 7px; height: 7px; }
  .card-back .contact { font-size: 4.4px; }

  /* Letterhead */
  .letterhead { left: 233px; top: 29px; width: 396px; height: 559px; }
  .letterhead .header { position: absolute; left: 24px; top: 34px; display: flex; align-items: center; gap: 8px; }
  .letterhead .brand { font-size: 13px; }
  .letterhead .brand-square { width: 8px; height: 8px; }
  .letterhead .contact { font-size: 4px; }

  /* Envelope back */
  .envelope-back { left: 679px; top: 79px; width: 485px; height: 235px; }
  .envelope-back svg { position: absolute; inset: 0; }

  /* Envelope front */
  .envelope-front { left: 679px; top: 336px; width: 485px; height: 245px; }
  .envelope-front .header { position: absolute; left: 22px; top: 24px; display: flex; align-items: center; gap: 8px; }
  .envelope-front .brand { font-size: 13px; }
  .envelope-front .brand-square { width: 8px; height: 8px; }
  .envelope-front .contact { font-size: 4.2px; }
</style>
</head>
<body>

  <section class="sheet card-front" aria-label="Business card front">
    <div class="brand"><span class="brand-square"></span>HARWELL</div>
    <div class="web">www.drharwell-example.com</div>
  </section>

  <section class="sheet card-back" aria-label="Business card back">
    <div class="brand"><span class="brand-square"></span>HARWELL</div>
    <div class="contact">
      <div class="name">Benedict Harwell, MD</div>
      <div>Torrance Ridge-Velmont Building</div>
      <div>Suite 460</div>
      <div>4127 Almaden Avenue</div>
      <div>La Jolla, CA 92037</div>
      <div>www.drharwell-example.com</div>
    </div>
  </section>

  <section class="sheet letterhead" aria-label="Letterhead">
    <div class="header">
      <div class="brand"><span class="brand-square"></span>HARWELL</div>
      <div class="contact">
        <div class="name">Benedict Harwell, MD</div>
        <div>Torrance Ridge-Velmont Building</div>
        <div>Suite 460, 4127 Almaden Avenue</div>
        <div>La Jolla, CA 92037</div>
        <div>www.drharwell-example.com</div>
      </div>
    </div>
  </section>

  <section class="sheet envelope-back" aria-label="Envelope back">
    <svg width="485" height="235" viewBox="0 0 485 235">
      <path d="M0 2 L230 66 Q242 70 254 66 L485 2" fill="none" stroke="var(--fold)" stroke-width="1.2"/>
      <path d="M0 2 L485 2" stroke="var(--fold)" stroke-width="1"/>
    </svg>
  </section>

  <section class="sheet envelope-front" aria-label="Envelope front">
    <div class="header">
      <div class="brand"><span class="brand-square"></span>HARWELL</div>
      <div class="contact">
        <div>Torrance Ridge-Velmont Building</div>
        <div>Suite 460</div>
        <div>4127 Almaden Avenue</div>
        <div>La Jolla, CA 92037</div>
      </div>
    </div>
  </section>

</body>
</html>
```